Travelogue book cover

The book is a collection of stories from my travels around the world. These stories run a full range of emotions from unbridled joy, to things that are much funnier today than they were at the time, to moments of sadness while reflecting on places that have been irrevocably changed. This world is an amazing and powerful place, and my stories tell its tale. The overall vibe is to love exploring the world, the thrill of discovery, the comedy of getting outside of your comfort zone, and just generally wanting to convey a sense of wonder and make people feel like they want to get out and explore for themselves.

The audience is in the 30-50 age target, educated, all genders, and either an experienced traveller or wishes they were.

On the style, I am looking for something that stands out when a reader is browsing Pellaro. Since most book covers are bright, full bleed and busy, I would prefer something that emphasizes white space and simplicity.

```html
<!DOCTYPE html>
<html lang="en">
<head>
<meta charset="utf-8">
<title>The Best Noodle House on the Wrong Side of Town — Book Cover</title>
<link rel="stylesheet" href="https://fonts.googleapis.com/css2?family=Cinzel:wght@400&family=Montserrat:wght@400;500&family=Tinos&display=swap">
<style>
  :root {
    --ink: #141414;
    --sky: #ebeaeb;
    --haze: #efeeef;
    --snow: #f5f4f5;
    --drift: #ecebec;
  }
  * { margin: 0; padding: 0; box-sizing: border-box; }
  html, body {
    width: 1200px;
    height: 844px;
    overflow: hidden;
    background: var(--snow);
  }
  .cover {
    position: relative;
    width: 1200px;
    height: 844px;
    overflow: hidden;
    color: var(--ink);
  }
  .scene {
    position: absolute;
    inset: 0;
    background:
      linear-gradient(180deg,
        var(--sky) 0%,
        var(--haze) 40%,
        var(--snow) 43%,
        var(--drift) 50%,
        var(--snow) 56%,
        var(--snow) 100%);
  }
  .back-tagline {
    position: absolute;
    left: 99px;
    top: 44px;
    font-family: "Montserrat", sans-serif;
    font-weight: 500;
    font-size: 18.2px;
    white-space: nowrap;
  }
  .back-blurb {
    position: absolute;
    left: 48px;
    top: 609px;
    width: 468px;
    font-family: "Tinos", "Times New Roman", serif;
    font-size: 19.4px;
    line-height: 19.6px;
    text-align: center;
  }
  .back-blurb p + p { margin-top: 19.6px; }
  .spine-title {
    position: absolute;
    left: 568px;
    top: 32px;
    writing-mode: vertical-rl;
    font-family: "Cinzel", serif;
    font-weight: 400;
    font-size: 25px;
    line-height: 30px;
    white-space: nowrap;
  }
  .spine-author {
    position: absolute;
    left: 590px;
    top: 594px;
    writing-mode: vertical-rl;
    font-family: "Montserrat", sans-serif;
    font-weight: 400;
    font-size: 15px;
    letter-spacing: 7.5px;
    white-space: nowrap;
  }
  .front-author {
    position: absolute;
    left: 773px;
    top: 28px;
    font-family: "Montserrat", sans-serif;
    font-weight: 400;
    font-size: 23px;
    letter-spacing: 10px;
    white-space: nowrap;
  }
  .front-title {
    position: absolute;
    left: 680px;
    width: 476px;
    top: 586px;
    text-align: center;
    font-family: "Cinzel", serif;
    font-weight: 400;
    font-size: 36px;
    line-height: 40px;
    letter-spacing: 0.5px;
  }
  .front-subtitle {
    position: absolute;
    left: 680px;
    width: 476px;
    top: 776px;
    text-align: center;
    font-family: "Cinzel", serif;
    font-weight: 400;
    font-size: 19.5px;
    letter-spacing: 0.4px;
    white-space: nowrap;
  }
</style>
</head>
<body>
  <main class="cover">
    <div class="scene" role="img" aria-label="Wide, misty snowfield under a pale grey sky, with a lone figure in dark winter clothes walking across the open white expanse"></div>

    <p class="back-tagline">FINDING YOURSELF BY GETTING LOST</p>

    <div class="back-blurb">
      <p>There’s nothing quite like travel to strip you down to your essential self.</p>
      <p>Whether you’re standing on the edge of an exploding volcano, or hopping on a plane to the most mysterious city in the world, it’s not always about what you see, but who you become.</p>
    </div>

    <h2 class="spine-title">THE BEST NOODLE HOUSE ON THE<br>WRONG SIDE OF TOWN</h2>
    <p class="spine-author">ELLIOT MARSH</p>

    <p class="front-author">ELLIOT MARSH</p>
    <h1 class="front-title">THE BEST<br>NOODLE HOUSE ON THE<br>WRONG SIDE OF TOWN</h1>
    <p class="front-subtitle">STORIES FROM A LIFE ON THE ROAD</p>
  </main>
</body>
</html>
```